Catholic composer needs poster for new musical, "THE STONE AND THE VIGIL, the Harvest Musical"

We need a dynamic poster for "The Stone and the Vigil," a new musical written for Catholic dinner theater. We need you to create an iconic design like you see in posters for classic musicals, like "Rosa Calendula," Lantern of the Harbour," or "Gilded." In our musical, “fire” represents the Holy Spirit, who showers man with his merciful love.

Miraculous events occur. A mighty wind from heaven fills the house. Tongues of fire appear over their heads. They speak in other tongues that are understandable by all present. They are emboldened to go out and tell the Good News to the world, despite the risks associated with evangelizing this fledgling religion. They exclaim, “Lord, you will show us the path to life.”

Target Market(s)

The audience is adult members of Catholic churches. But don't make the design look too "churchy."

Requirements
Must have
• Photoshop or Illustrated file with layers, or vector format.
Should not have
• Really don't want photos.

```html
<!DOCTYPE html>
<html lang="en">
<head>
<meta charset="utf-8">
<title>The Stone and the Vigil — The Harvest Musical</title>
<link rel="stylesheet" href="https://fonts.googleapis.com/css2?family=Anton&family=Roboto+Condensed:wght@400;700&family=Dancing+Script:wght@700&display=swap">
<style>
  :root {
    --paper: #f7f5f0;
    --paper-edge: #e9e6de;
    --ink: #1c1a19;
    --crimson: #c4161c;
    --glow: #f6d84a;
    --rule: #9a9692;
    --muted: #4a4644;
    --shadow-tone: #1e1c1b;
  }
  * { box-sizing: border-box; margin: 0; padding: 0; }
  html, body { width: 789px; height: 1200px; overflow: hidden; background: var(--paper); }
  .poster {
    position: relative;
    width: 789px;
    height: 1200px;
    background: radial-gradient(ellipse at 50% 40%, var(--paper) 55%, var(--paper-edge) 100%);
    font-family: "Roboto Condensed", sans-serif;
    color: var(--ink);
    overflow: hidden;
  }
  .heart-art {
    position: absolute;
    left: 60px; top: 90px;
    width: 400px; height: 360px;
    border-radius: 50%;
    background: radial-gradient(circle, var(--crimson) 0%, var(--crimson) 30%, rgba(246,216,74,0.8) 48%, rgba(246,216,74,0) 72%);
  }
  .title {
    position: absolute;
    left: 305px; top: 470px;
    line-height: 1;
  }
  .title-small {
    display: block;
    font-family: "Anton", sans-serif;
    font-size: 34px;
    text-transform: uppercase;
    letter-spacing: 1px;
  }
  .title-row { display: flex; align-items: flex-end; gap: 6px; }
  .title-word {
    display: block;
    font-family: "Anton", sans-serif;
    font-size: 118px;
    color: var(--crimson);
    text-transform: uppercase;
    letter-spacing: 1px;
    line-height: 0.95;
  }
  .title-amp {
    font-family: "Anton", sans-serif;
    font-size: 34px;
    margin-bottom: 12px;
  }
  .subtitle {
    display: block;
    font-family: "Anton", sans-serif;
    font-size: 30px;
    letter-spacing: 1px;
    margin-top: 6px;
  }
  .figure-art {
    position: absolute;
    left: 20px; top: 860px;
    width: 250px; height: 320px;
    background: linear-gradient(180deg, #2e2b2a, var(--shadow-tone));
  }
  .details {
    position: absolute;
    left: 305px; top: 875px;
    width: 430px;
  }
  .tagline {
    font-size: 14px;
    font-weight: 700;
    letter-spacing: 1.5px;
    text-transform: uppercase;
    color: var(--muted);
  }
  .quote {
    margin-top: 14px;
    font-family: "Dancing Script", cursive;
    font-size: 26px;
    color: var(--crimson);
    line-height: 1.1;
  }
  .info-list { list-style: none; margin-top: 16px; }
  .info-list li {
    display: flex;
    align-items: flex-end;
    gap: 10px;
    height: 28px;
    font-size: 14px;
    font-weight: 700;
    color: var(--muted);
  }
  .info-list li::after {
    content: "";
    flex: 1;
    border-bottom: 1px solid var(--rule);
    margin-bottom: 4px;
  }
  .website {
    position: absolute;
    left: 305px; top: 1130px;
    font-size: 16px;
    font-weight: 700;
    letter-spacing: 0.5px;
  }
</style>
</head>
<body>
  <main class="poster">
    <div class="heart-art" role="img" aria-label="Illustration of a cracked red heart mended with a bandage, glowing yellow"></div>

    <h1 class="title">
      <span class="title-small">The</span>
      <span class="title-row"><span class="title-word">Stone</span><span class="title-amp">&amp;</span></span>
      <span class="title-small">The</span>
      <span class="title-word">Vigil</span>
      <span class="subtitle">THE HARVEST MUSICAL</span>
    </h1>

    <div class="figure-art" role="img" aria-label="Dark silhouette illustration of a kneeling figure in prayer"></div>

    <section class="details">
      <p class="tagline">A new musical for Catholic dinner theater</p>
      <p class="quote">“Lord, you will show us the path to life.”</p>
      <ul class="info-list">
        <li>Date</li>
        <li>Time</li>
        <li>Place</li>
        <li>Tickets</li>
      </ul>
    </section>

    <p class="website">www.thestoneandthevigil.com</p>
  </main>
</body>
</html>
```